Boutique Shoe Bag Race wear Business Card Design

We are a new luxury shoe bag, jewellery and race wear store stocking local and international designers. Located in the fashion precinct of beautiful Calloway Cove famous in Sydney Australia. Stocking French jewellery and shoes such as Renaud valmiers plus Australian made. Looking at quality and service and looking after the locals and tourists.
Ideas: White background, Black writing in bold engravers, logo in middle of Marlow and Boutique a gold horseshoe (facing upright so the curve is at the bottom) with a black stiletto inside. French clover silver and black border (not irish clover the French lattice type look)
Updates

Marlow Atelier

I open 8/4 so require business card design ASAP.

Please place gold horseshoe facing upwards with the black stiletto inside.

Bold engravers writing for business name.

I will have my phone number tomorrow to update.

Border in similar/same style as attached picture with black/silver clover French design.

Thank you. Tessa                                   

Industry/Entity Type

Fashion

Contact Information for Business Card

Marlow Atelier
Boutique Owner Tessa Wrenfield
41B Parrin Lane
Calloway Cove NSW 2093 Australia
0471239046
02 **** *TBA
info@marlowatelier.com.au
Facebook.com/MarlowAtelier
www.marlowatelier.com.au

Font styles to use
Other font styles liked:
• Bold Engravers

Requirements
Must have
• Info on one side including business name and logo with black stiletto and gold horse shoe. reverse side with French clover border and Larger name Marlow Atelier with logo in centre.
Should not have
• irish clover
French script
horseshoe upside down

```html
<!DOCTYPE html>
<html lang="en">
<head>
<meta charset="utf-8">
<title>Marlow Atelier Business Card</title>
<link rel="stylesheet" href="https://fonts.googleapis.com/css2?family=Cinzel:wght@400;700&display=swap">
<style>
  :root {
    --backdrop: #ededed;
    --card: #ffffff;
    --ink: #111111;
    --gold: #c9a227;
    --lattice: #d9d9d9;
  }
  html, body {
    margin: 0;
    padding: 0;
    overflow: hidden;
  }
  body {
    width: 1200px;
    height: 768px;
    background: var(--backdrop);
    position: relative;
    font-family: "Cinzel", serif;
    color: var(--ink);
  }
  .card {
    position: absolute;
    width: 541px;
    height: 331px;
    background: var(--card);
  }
  .card--front { left: 42px; top: 176px; }
  .card--back { left: 615px; top: 287px; }

  .brand {
    position: absolute;
    left: 0;
    right: 0;
    display: flex;
    align-items: center;
    justify-content: center;
    gap: 12px;
  }
  .brand__dot {
    width: 22px;
    height: 22px;
    border-radius: 50%;
    background: var(--gold);
    flex: none;
  }
  .brand__name {
    font-weight: 700;
    letter-spacing: 0.06em;
    text-transform: uppercase;
    white-space: nowrap;
  }
  .card--front .brand { top: 66px; }
  .card--front .brand__name { font-size: 21px; }

  .owner {
    position: absolute;
    left: 0;
    right: 0;
    top: 133px;
    text-align: center;
  }
  .owner__name {
    margin: 0;
    font-size: 19px;
    font-weight: 700;
    letter-spacing: 0.05em;
    text-transform: uppercase;
  }
  .owner__role {
    margin: 4px 0 0;
    font-size: 11px;
    font-weight: 700;
    letter-spacing: 0.06em;
    text-transform: uppercase;
  }

  .contact {
    position: absolute;
    left: 0;
    right: 0;
    top: 202px;
    margin: 0;
    padding: 0;
    list-style: none;
    text-align: center;
    font-size: 12.5px;
    font-variant: small-caps;
    line-height: 19.5px;
    letter-spacing: 0.03em;
  }

  .lattice-border {
    position: absolute;
    inset: 0;
  }
  .card--back .brand {
    top: 50%;
    transform: translateY(-50%);
  }
  .card--back .brand__name { font-size: 27px; }
  .card--back .brand__dot { width: 26px; height: 26px; }
</style>
</head>
<body>

  <section class="card card--front" aria-label="Business card front">
    <div class="brand">
      <span class="brand__dot"></span>
      <span class="brand__name">Marlow Atelier</span>
    </div>
    <div class="owner">
      <h1 class="owner__name">Tessa Wrenfield</h1>
      <p class="owner__role">Botique Owner</p>
    </div>
    <ul class="contact">
      <li>41B Parrin Lane Calloway Cove NSW 2093 Australia</li>
      <li>0471239046 02 **** *TBA</li>
      <li>info@marlowatelier.com.au</li>
      <li>Facebook.com/MarlowAtelier</li>
      <li>www.marlowatelier.com.au</li>
    </ul>
  </section>

  <section class="card card--back" aria-label="Business card back">
    <svg class="lattice-border" width="541" height="331" viewBox="0 0 541 331" role="img" aria-label="Silver French quatrefoil lattice border framing the card">
      <path fill="var(--lattice)" fill-rule="evenodd"
            d="M10 10 H531 V321 H10 Z M70 70 V261 H471 V70 Z"/>
    </svg>
    <div class="brand">
      <span class="brand__dot"></span>
      <span class="brand__name">Marlow Atelier</span>
    </div>
  </section>

</body>
</html>
```